Hair extensions packaging design

Professional hair extensions packaging design.
We like a clean and crisp look. The design should convey luxury and highest quality.

Target Market(s)

women ages 16-40

Industry/Entity Type

beauty, hair

Font styles to use
Other font styles liked:
• kiona

Requirements
Must have
• clean, crisp, professional look

```html
<!DOCTYPE html>
<html lang="en">
<head>
<meta charset="utf-8">
<title>Velora Hair Extension Pouch</title>
<link rel="stylesheet" href="https://fonts.googleapis.com/css2?family=Josefin+Sans:wght@300;400&family=Oswald:wght@300;400&family=Open+Sans:wght@400;600&display=swap">
<style>
  :root {
    --bg: #d9d9d9;
    --pouch-white: #ffffff;
    --pouch-clear: #e9e9ea;
    --seal: #f1f1f2;
    --gold: #c49a4a;
    --ink: #1b1b1b;
    --body-ink: #2a2a2a;
    --badge-black: #161616;
    --bronze: #b5651d;
    --bronze-dark: #5a2a0c;
    --rule: #555555;
  }
  * { margin: 0; padding: 0; box-sizing: border-box; }
  html, body { width: 1200px; height: 1000px; overflow: hidden; background: var(--bg); }
  .canvas { position: relative; width: 1200px; height: 1000px; }
  .pouch { position: absolute; left: 300px; top: 70px; width: 600px; height: 860px; border-radius: 10px; overflow: hidden; }
  .pouch-art { position: absolute; inset: 0; }
  .brand-name {
    position: absolute; top: 98px; left: 0; width: 600px; text-align: center;
    font-family: 'Josefin Sans', sans-serif; font-weight: 300; font-size: 28px;
    letter-spacing: 7px; color: var(--gold);
  }
  .tagline {
    position: absolute; top: 175px; left: 0; width: 600px; text-align: center;
    font-family: 'Oswald', sans-serif; font-weight: 300; font-size: 15px;
    letter-spacing: 0.3px; color: var(--gold);
  }
  .headline {
    position: absolute; top: 224px; left: 0; width: 600px; text-align: center;
    font-family: 'Josefin Sans', sans-serif; font-weight: 300; font-size: 48px;
    letter-spacing: 7px; color: var(--ink);
  }
  .subhead {
    position: absolute; left: 0; width: 600px; text-align: center;
    font-family: 'Josefin Sans', sans-serif; font-weight: 300; font-size: 25px;
    letter-spacing: 5px; color: var(--ink);
  }
  .subhead.line-one { top: 284px; }
  .subhead.line-two { top: 317px; }
  .divider { position: absolute; top: 351px; left: 143px; width: 332px; border-top: 2px dotted var(--rule); }
  .product-copy {
    position: absolute; top: 358px; left: 143px; width: 340px;
    font-family: 'Open Sans', sans-serif; font-size: 12px; line-height: 15.4px; color: var(--body-ink);
    white-space: nowrap;
  }
  .product-copy .site { font-weight: 600; }
  .shade-badge {
    position: absolute; left: 50px; top: 407px; width: 94px; height: 94px; border-radius: 50%;
    background: var(--badge-black); border: 5px solid var(--bronze);
    box-shadow: 0 0 0 2px var(--bronze-dark);
    display: flex; align-items: center; justify-content: center; text-align: center;
    font-family: 'Oswald', sans-serif; font-weight: 300; font-size: 19px; line-height: 19px; color: #fff;
  }
</style>
</head>
<body>
<main class="canvas">
  <section class="pouch">
    <svg class="pouch-art" width="600" height="860" viewBox="0 0 600 860">
      <defs>
        <linearGradient id="band" x1="0" x2="1" y1="0" y2="0">
          <stop offset="0" stop-color="#e07a1f"/>
          <stop offset="0.35" stop-color="#f29a2e"/>
          <stop offset="0.6" stop-color="#8a3a12"/>
          <stop offset="1" stop-color="#2a0f05"/>
        </linearGradient>
        <linearGradient id="hair-tone" x1="0" x2="0" y1="0" y2="1">
          <stop offset="0" stop-color="#a8703f"/>
          <stop offset="0.7" stop-color="#a0683a"/>
          <stop offset="1" stop-color="#6e4324"/>
        </linearGradient>
      </defs>
      <rect class="clear-window" x="0" y="0" width="600" height="860" fill="var(--pouch-clear)"/>
      <rect class="hair-photo" role="img" aria-label="Photo of four straight medium light brown hair extension wefts"
            x="128" y="420" width="357" height="378" rx="18" fill="url(#hair-tone)"/>
      <path class="label-band" d="M0 402 Q290 568 600 398 L600 412 Q290 582 0 416 Z" fill="url(#band)"/>
      <path class="label-white" d="M0 0 H600 V398 Q290 568 0 402 Z" fill="var(--pouch-white)"/>
      <rect class="bottom-seal" x="0" y="826" width="600" height="34" fill="var(--seal)"/>
    </svg>

    <div class="brand-name">VELORA</div>
    <div class="tagline">LUXURY . 100% REMI &nbsp;. HAIR COUTURE</div>
    <h1 class="headline">100% VIRGIN</h1>
    <div class="subhead line-one">REMI HUMAN HAIR</div>
    <div class="subhead line-two">EXTENTION</div>
    <div class="divider"></div>
    <p class="product-copy">
      We GUARENTEE the highest quality of our products<br>
      Highest Quality, Double Drawn, 100% Human Remi Hair<br>
      <span class="site">www.velorahair.com</span><br>
      Velora hair is cut directly from the donor to ensure<br>
      the cuticle remains in tact and the hair will never tangle!
    </p>
    <div class="shade-badge">Medium<br>Light<br>Brown</div>
  </section>
</main>
</body>
</html>
```